Company providing Business Management Services needs modern business card

The business provides services like tender preparation, bank submissions, business health checks, financial and admin support. We want to portray 'Trust', 'Strength' and 'Support'.
2 styles of logo in various formats have been uploaded.
Looking for easy to understand, yet sophisticated and stand out from the crowd.

Target Market(s)

Small and Medium sized businesses

Industry/Entity Type

Business

Contact Information for Business Card

Name - Daniel Vesterby, Description - Manager, Phone - 0472 915 603, Email - danielvesterby@kpwholdingsgroup.example, Work description - Business Management Services.

Requirements
Must have
• Logo

```html
<!DOCTYPE html>
<html lang="en">
<head>
<meta charset="utf-8">
<title>KPW Holdings Group – Business Card</title>
<link rel="stylesheet" href="https://fonts.googleapis.com/css2?family=Carlito:wght@400;700&display=swap">
<style>
  :root {
    --page-bg: #2a2a2a;
    --card-bg: #ffffff;
    --top-band: #1aa7e6;
    --ink-dark: #1e1e1e;
    --ink-logo: #555759;
    --bar-purple: #8e3a9d;
    --bar-blue: #2b5aa8;
    --bar-green: #4aa84a;
    --bar-orange: #f07a22;
    --deco-grey: #b9b9b9;
    --deco-light: #e6e6e6;
  }
  * { box-sizing: border-box; margin: 0; padding: 0; }
  html, body {
    width: 1200px;
    height: 1024px;
    overflow: hidden;
    background: var(--page-bg);
    font-family: "Carlito", "Calibri", sans-serif;
  }
  .business-card {
    position: absolute;
    left: 80px;
    top: 217px;
    width: 1040px;
    height: 590px;
    background: var(--card-bg);
    overflow: hidden;
  }
  .top-band {
    position: absolute;
    left: 0; top: 0;
    width: 100%;
    height: 19px;
    background: var(--top-band);
  }
  .contact-block {
    position: absolute;
    top: 62px;
    left: 0;
    width: 100%;
    text-align: center;
    color: var(--ink-dark);
  }
  .person-name {
    font-size: 37px;
    font-weight: 400;
    line-height: 1.05;
  }
  .person-name .first { font-weight: 700; }
  .person-role {
    font-size: 24px;
    line-height: 1.05;
  }
  .person-phone {
    font-size: 22px;
    font-weight: 700;
    line-height: 1.1;
  }
  .brand {
    position: absolute;
    top: 230px;
    left: 0;
    width: 100%;
    display: flex;
    justify-content: center;
    align-items: center;
    gap: 22px;
  }
  .brand-square {
    width: 54px;
    height: 54px;
    background: var(--ink-logo);
  }
  .brand-name {
    font-size: 58px;
    font-weight: 700;
    color: var(--ink-logo);
    line-height: 1;
  }
  .service-line {
    position: absolute;
    top: 362px;
    left: 0;
    width: 100%;
    text-align: center;
    font-size: 31px;
    font-weight: 700;
    color: var(--ink-dark);
  }
  .email {
    position: absolute;
    top: 478px;
    left: 0;
    width: 100%;
    text-align: center;
    font-size: 26px;
    font-weight: 700;
    color: var(--ink-dark);
  }
  .side-motif {
    position: absolute;
    background: linear-gradient(135deg, var(--deco-light), var(--deco-grey));
  }
  .side-motif.left {
    left: 0;
    top: 150px;
    width: 190px;
    height: 330px;
    clip-path: polygon(0 0, 20% 0, 100% 50%, 20% 100%, 0 100%);
  }
  .side-motif.right {
    right: 0;
    top: 175px;
    width: 190px;
    height: 300px;
    clip-path: polygon(100% 0, 80% 0, 0 50%, 80% 100%, 100% 100%);
  }
  .colour-bar {
    position: absolute;
    left: 0;
    bottom: 0;
    width: 100%;
    height: 75px;
    display: flex;
  }
  .colour-bar span { display: block; height: 100%; }
  .colour-bar .purple { width: 128px; background: var(--bar-purple); }
  .colour-bar .blue { width: 256px; background: var(--bar-blue); }
  .colour-bar .green { width: 315px; background: var(--bar-green); }
  .colour-bar .orange { flex: 1; background: var(--bar-orange); }
</style>
</head>
<body>
  <div class="business-card">
    <div class="top-band"></div>

    <div class="side-motif left" role="img" aria-label="Striped chevron decoration pointing inward"></div>
    <div class="side-motif right" role="img" aria-label="Striped chevron decoration pointing inward"></div>

    <div class="contact-block">
      <p class="person-name"><span class="first">Daniel</span> Vesterby</p>
      <p class="person-role">Manager</p>
      <p class="person-phone">0472 915 603</p>
    </div>

    <div class="brand">
      <div class="brand-square"></div>
      <p class="brand-name">KPW Holdings Group</p>
    </div>

    <p class="service-line">Business Management Services</p>

    <p class="email">danielvesterby@kpwholdingsgroup.example</p>

    <div class="colour-bar">
      <span class="purple"></span>
      <span class="blue"></span>
      <span class="green"></span>
      <span class="orange"></span>
    </div>
  </div>
</body>
</html>
```